2023 Cheers to 50 Years Graphic

Hi - I'd like a high-res image that's also print ready that we can use around our office with our 2023 slogan: Cheers to 50 years!

Ideally we'd like a catchy image, the slogan and our logo.

I'll attach the 2022 example. Please use our 50th anniversary logo also attached.

Graphic could be anything celebratory!

Main demographic is males.

Maybe cheers of champagne glasses or beer. But open top option that does not involve alcohol too.

```html
<!DOCTYPE html>
<html lang="en">
<head>
<meta charset="utf-8">
<title>2023 Cheers to 50 Years</title>
<link rel="stylesheet" href="https://fonts.googleapis.com/css2?family=Lobster&display=swap">
<style>
  :root {
    --ink: #2e3a84;
    --spark-core: #ffffff;
    --spark-glow: #fff3de;
    --spark-warm: #f8cf92;
    --spark-amber: #e59d4e;
    --spark-copper: #b8692a;
    --spark-deep: #5e3012;
  }
  html, body {
    margin: 0;
    padding: 0;
    overflow: hidden;
    background: #ffffff;
  }
  .poster {
    position: relative;
    width: 1200px;
    height: 800px;
    overflow: hidden;
    font-family: "Lobster", cursive;
    color: var(--ink);
  }
  .sparkler-backdrop {
    position: absolute;
    inset: 0;
    background:
      radial-gradient(ellipse 34% 30% at 52% 38%, var(--spark-core) 0%, var(--spark-core) 55%, rgba(255,255,255,0) 100%),
      radial-gradient(ellipse 30% 28% at 70% 62%, var(--spark-core) 0%, rgba(255,255,255,0.9) 45%, rgba(255,255,255,0) 100%),
      radial-gradient(ellipse 22% 18% at 40% 8%, rgba(255,255,255,0.95) 0%, rgba(255,255,255,0) 100%),
      radial-gradient(ellipse 26% 34% at 0% 100%, var(--spark-deep) 0%, rgba(94,48,18,0.6) 45%, rgba(94,48,18,0) 100%),
      radial-gradient(ellipse 18% 40% at 0% 45%, rgba(138,74,28,0.85) 0%, rgba(138,74,28,0) 100%),
      radial-gradient(ellipse 20% 30% at 100% 12%, rgba(184,105,42,0.8) 0%, rgba(184,105,42,0) 100%),
      radial-gradient(ellipse 30% 20% at 30% 100%, rgba(184,105,42,0.7) 0%, rgba(184,105,42,0) 100%),
      radial-gradient(ellipse 80% 78% at 58% 45%, var(--spark-glow) 0%, var(--spark-warm) 45%, var(--spark-amber) 72%, var(--spark-copper) 100%);
  }
  .brand-mark {
    position: absolute;
    left: 853px;
    top: 48px;
    width: 272px;
    height: 150px;
    display: flex;
    align-items: center;
    justify-content: center;
    gap: 16px;
    color: var(--ink);
  }
  .brand-mark .brand-dot {
    flex: none;
    width: 30px;
    height: 30px;
    border-radius: 50%;
    background: var(--ink);
  }
  .brand-mark .brand-name {
    font-size: 44px;
    line-height: 1.05;
  }
  .headline {
    position: absolute;
    margin: 0;
    font-weight: 400;
    text-shadow: 0 0 14px rgba(255,255,255,0.7);
    white-space: nowrap;
  }
  .headline-year {
    top: 205px;
    left: 420px;
    font-size: 142px;
    line-height: 1;
  }
  .headline-slogan {
    top: 362px;
    left: 99px;
    font-size: 134px;
    line-height: 1;
  }
</style>
</head>
<body>
  <main class="poster">
    <div class="sparkler-backdrop" role="img" aria-label="Close-up of a glowing golden sparkler bursting with bright sparks"></div>

    <div class="brand-mark">
      <span class="brand-dot"></span>
      <span class="brand-name">Harborline<br>Supply</span>
    </div>

    <h1 class="headline headline-year">2023</h1>
    <p class="headline headline-slogan">Cheers to 50 years!</p>
  </main>
</body>
</html>
```